Webpage for a treatment housing for young addicts.

I need a new design and files for my wordpress page. I need it to be more neat and clean. I need it to look professional with a starting page that will work as a navigation. I need like logo and phone number and such up top, a picture under it with one sentence as a slogan and under it 6 boxes to click to come to our different pages. Under it I want news etc.

Target Market(s)

Social services, employees and governements

Coding

Coded - Design and coding required

Font styles to use
Sans Serif

Colors
abd037
3176b5
9d9d9d
aaaaaa
f04a50

Requirements
Must have
• A nice design
Nice to have
• need it to look professional with a starting page that will work as a navigation. I need like logo and phone number and such up top, a picture under it with one sentence as a slogan and under it 6 boxes to click to come to our different pages. Under it I want news etc.
• today www.kelmora.se
• want more like www.trivest.se or www.solbrink.se
Should not have
• To many different colours and a messy design.

```html
<!DOCTYPE html>
<html lang="en">
<head>
<meta charset="utf-8">
<title>Kelmora – Care and Housing</title>
<link href="https://fonts.googleapis.com/css2?family=Josefin+Sans:wght@600;700&family=Montserrat:wght@400;500;600;700&display=swap" rel="stylesheet">
<style>
:root{
  --green:#8ab52d;
  --blue:#2e5ea6;
  --blue-dark:#263f7a;
  --grey:#9d9d9d;
  --grey-light:#aaaaaa;
  --panel:#cfd1cb;
  --card:#f3f2f2;
  --ink:#1c1c1c;
  --text:#666;
  --topbar:#d9d9d9;
  --foot:#222;
}
*{box-sizing:border-box;margin:0;padding:0}
html,body{width:1200px;height:2721px;overflow:hidden;background:#fff}
body{font-family:'Montserrat',sans-serif;color:var(--text);position:relative}
.abs{position:absolute}
.btn{position:absolute;display:flex;align-items:center;justify-content:center;background:var(--blue);color:#fff;border-radius:20px;font-weight:700;letter-spacing:.6px;font-size:15px}

/* header */
.site-header{position:absolute;left:0;top:0;width:1200px;height:112px;background:#fff}
.brand{left:24px;top:34px;display:flex;align-items:center;gap:12px}
.brand-dot{width:38px;height:38px;border-radius:50%;background:var(--green)}
.brand-name{font-family:'Montserrat',sans-serif;font-weight:700;font-size:34px;color:var(--blue)}
.news-bar{left:297px;top:0;width:610px;height:39px;background:var(--topbar);display:flex;align-items:center;padding-left:16px;font-size:12px;color:#333}
.news-bar b{font-size:15px;font-weight:700;color:#222;margin-right:12px;padding-right:14px;border-right:2px solid #222;line-height:18px}
.tab{top:0;height:39px;display:flex;align-items:center;justify-content:center;gap:8px;color:#fff;font-size:13px;font-weight:700;letter-spacing:1px}
.tab-treat{left:907px;width:151px;background:var(--green)}
.tab-contact{left:1058px;width:142px;background:var(--blue)}
.info-row{top:39px;height:73px;display:flex;align-items:center;gap:12px;font-weight:700;color:#555;font-size:15px;letter-spacing:.8px}
.vline{top:39px;width:1px;height:73px;background:#ccc}

/* hero */
.hero{position:absolute;left:0;top:112px;width:1200px;height:463px;background:linear-gradient(100deg,#4f4d48 0%,#8c8a82 18%,#c3c6c8 40%,#dcdfe2 62%,#e6e8ea 80%,#cfd2d2 100%)}
.hero-snow{left:400px;top:340px;width:800px;height:123px;background:linear-gradient(180deg,rgba(120,110,100,0) 0%,rgba(150,140,130,.55) 60%,rgba(200,200,200,.7) 100%)}
.hero h1{position:absolute;left:633px;top:98px;width:560px;white-space:nowrap;font-family:'Josefin Sans',sans-serif;font-weight:700;font-size:40px;line-height:50px;color:#111;letter-spacing:1.5px}
.hero h1 em{font-style:normal;color:var(--green);font-size:50px;letter-spacing:1px}

/* nav tiles */
.tiles{position:absolute;left:0;top:575px;width:1200px;height:569px;background:var(--panel)}
.tile{position:absolute;width:256px;height:206px;background:var(--card);border:2px solid #e2e2e2;display:flex;flex-direction:column;align-items:center}
.tile svg{margin-top:16px}
.tile h3{margin-top:14px;text-align:center;font-size:22px;font-weight:700;color:#8a8a8a;letter-spacing:1.5px;line-height:26px}
.tile.active{border-color:var(--blue)}
.tile.active h3{color:var(--blue-dark)}
.tile .go{position:absolute;bottom:-15px;left:113px;width:30px;height:30px;border-radius:50%;background:var(--blue-dark);display:flex;align-items:center;justify-content:center}

/* news */
.section-title{position:absolute;font-family:'Josefin Sans',sans-serif;font-weight:700;font-size:38px;color:#111;letter-spacing:1.5px}
.title-bar{position:absolute;width:40px;height:4px;background:var(--green)}
.news-card{position:absolute;top:1308px;width:270px}
.news-img{width:270px;height:168px}
.news-card h4{margin-top:16px;font-size:15px;font-weight:700;color:var(--blue-dark);text-decoration:underline;letter-spacing:.6px}
.news-card time{display:block;margin-top:10px;font-size:11px;color:#999;letter-spacing:.5px}
.news-card p{margin-top:12px;width:245px;font-size:13px;line-height:17px;color:#777}

/* about */
.about{position:absolute;left:0;top:1710px;width:1200px;height:417px;background:var(--panel)}
.about-text{position:absolute;left:189px;top:166px;width:540px;font-size:13.5px;line-height:21px;color:#444;letter-spacing:.3px}
.about-text b{color:#222}
.play{position:absolute;width:36px;height:36px;border-radius:50%;background:rgba(255,255,255,.9);display:flex;align-items:center;justify-content:center}

/* footer */
.foot-logo{left:185px;top:2190px;display:flex;align-items:center;gap:12px}
.foot-logo .brand-dot{background:var(--grey-light);width:44px;height:44px}
.foot-logo .brand-name{color:var(--grey-light);font-size:40px}
.foot-h{position:absolute;top:2296px;font-size:20px;font-weight:700;color:#222;letter-spacing:1px}
.foot-h::after{content:"";position:absolute;left:0;top:34px;width:38px;height:3px;background:#222}
.contact-line{position:absolute;left:174px;display:flex;gap:14px;font-size:13px;font-weight:700;color:#555;line-height:24px;letter-spacing:.6px}
.links{position:absolute;left:466px;top:2346px;list-style:none;font-size:13.5px;line-height:27.5px;color:#777;letter-spacing:.6px}
.subscribe{position:absolute;left:758px;top:2408px;width:270px;height:38px;border:2px solid var(--blue-dark);border-radius:4px}
.subscribe span{position:absolute;left:16px;top:9px;font-style:italic;font-size:13px;color:#888}
.subscribe b{position:absolute;right:3px;top:3px;width:70px;height:28px;background:var(--blue);color:#fff;font-size:12px;display:flex;align-items:center;justify-content:center;border-radius:2px}
.social{position:absolute;top:2546px;width:70px;height:70px;border-radius:50%}
.social i{position:absolute;right:-6px;bottom:-8px;width:26px;height:26px;border-radius:50%;border:2px solid #fff}
.copyright{position:absolute;left:0;top:2675px;width:1200px;height:46px;background:var(--foot);color:#eee;font-size:12px;display:flex;align-items:center;justify-content:center;letter-spacing:.5px}
</style>
</head>
<body>

<header class="site-header">
  <div class="abs brand"><span class="brand-dot"></span><span class="brand-name">Kelmora</span></div>
  <div class="abs news-bar"><b>Latest News</b>Ut enim ad minima veniam, quis nostrum ....</div>
  <div class="abs tab tab-treat">
    <svg width="18" height="14" viewBox="0 0 18 14"><path d="M1 2 C8 0 16 2 17 12 C10 12 4 9 1 2Z" fill="#1d3a14"/></svg>TREATMENT</div>
  <div class="abs tab tab-contact">
    <svg width="16" height="14" viewBox="0 0 16 14" fill="none" stroke="#fff" stroke-width="1.4"><path d="M1 7 L15 1 L10 13 L7 8 Z"/></svg>CONTACT</div>

  <div class="abs info-row" style="left:612px">
    <svg width="34" height="34" viewBox="0 0 34 34" fill="none" stroke="#777" stroke-width="2"><path d="M8 4 L13 10 L10 14 C12 19 15 22 20 24 L24 21 L30 26 L27 31 C15 30 4 19 3 8 Z"/><path d="M20 5 A10 10 0 0 1 29 14"/><path d="M19 10 A5 5 0 0 1 24 15"/></svg>
    <span>010-4417260</span>
  </div>
  <div class="abs vline" style="left:805px"></div>
  <div class="abs info-row" style="left:822px;font-size:13px;line-height:22px">
    <svg width="40" height="40" viewBox="0 0 40 40" fill="none" stroke="#777" stroke-width="3"><circle cx="20" cy="20" r="17"/><path d="M20 9 V20 H28"/></svg>
    <span>Monday to Friday<br>9AM - 6PM</span>
  </div>
  <div class="abs vline" style="left:1021px"></div>
  <svg class="abs" style="left:1044px;top:55px" width="44" height="44" viewBox="0 0 44 44" fill="none" stroke="#555" stroke-width="3.2"><circle cx="18" cy="18" r="15"/><path d="M29 29 L41 41"/></svg>
  <div class="abs vline" style="left:1111px"></div>
  <svg class="abs" style="left:1135px;top:57px" width="42" height="36" viewBox="0 0 42 36" fill="#555"><rect y="0" width="42" height="4.5"/><rect y="15" width="42" height="4.5"/><rect y="30" width="42" height="4.5"/></svg>
</header>

<section class="hero" role="img" aria-label="Photograph of a hiker with a backpack sitting on a rocky cliff above snowy mountains under a cloudy sky">
  <div class="abs hero-snow"></div>
  <h1>We create <em>sustainable</em><br><em>pathways</em> to a better<br>future</h1>
  <a class="btn" style="left:634px;top:280px;width:172px;height:44px;font-size:16px">LEARN MORE</a>
</section>

<section class="tiles">
  <div class="tile" style="left:185px;top:60px">
    <svg width="70" height="80" viewBox="0 0 70 80" fill="none" stroke="#999" stroke-width="3"><path d="M35 3 L64 13 V40 C64 58 50 70 35 77 C20 70 6 58 6 40 V13 Z"/><path d="M35 13 L55 20 V40 C55 53 46 62 35 67 C24 62 15 53 15 40 V20 Z"/><circle cx="35" cy="40" r="16"/><path d="M27 40 L33 46 L43 35"/></svg>
    <h3>Quality<br>Work</h3><span class="go"><svg width="10" height="12" viewBox="0 0 10 12" fill="none" stroke="#fff" stroke-width="2"><path d="M3 1 L8 6 L3 11"/></svg></span>
  </div>
  <div class="tile" style="left:472px;top:60px">
    <svg width="70" height="70" viewBox="0 0 70 70"><path d="M2 6 C30 2 66 10 68 50 C46 58 20 46 12 26 C24 32 32 38 40 50 C36 34 24 22 2 6Z" fill="#888"/><path d="M30 40 L20 66" stroke="#888" stroke-width="3"/></svg>
    <h3>Treatment</h3><span class="go"><svg width="10" height="12" viewBox="0 0 10 12" fill="none" stroke="#fff" stroke-width="2"><path d="M3 1 L8 6 L3 11"/></svg></span>
  </div>
  <div class="tile" style="left:764px;top:60px">
    <svg width="76" height="72" viewBox="0 0 76 72" fill="none" stroke="#999" stroke-width="2.5"><path d="M38 2 V12 M16 10 L22 18 M60 10 L54 18 M2 34 H10 M66 34 H74"/><path d="M18 26 H58 L66 36 L38 66 L10 36 Z M10 36 H66 M28 26 L24 36 L38 66 L52 36 L48 26"/></svg>
    <h3>Our Values</h3><span class="go"><svg width="10" height="12" viewBox="0 0 10 12" fill="none" stroke="#fff" stroke-width="2"><path d="M3 1 L8 6 L3 11"/></svg></span>
  </div>
  <div class="tile" style="left:185px;top:301px">
    <svg width="84" height="74" viewBox="0 0 84 74" fill="#888"><rect x="40" y="6" width="4" height="62"/><circle cx="42" cy="6" r="5"/><rect x="10" y="16" width="64" height="4"/><rect x="22" y="66" width="40" height="6"/><path d="M4 48 L16 20 L28 48 Z M56 48 L68 20 L80 48 Z" fill="none" stroke="#888" stroke-width="2.5"/><path d="M2 48 H30 C28 58 4 58 2 48Z M54 48 H82 C80 58 56 58 54 48Z"/></svg>
    <h3>Ethical<br>Approach</h3><span class="go"><svg width="10" height="12" viewBox="0 0 10 12" fill="none" stroke="#fff" stroke-width="2"><path d="M3 1 L8 6 L3 11"/></svg></span>
  </div>
  <div class="tile" style="left:472px;top:301px">
    <svg width="72" height="74" viewBox="0 0 72 74" fill="none" stroke="#999" stroke-width="2.5"><path d="M22 70 V58 C12 52 6 42 8 30 C10 14 24 4 38 4 C54 4 66 16 66 32 C66 44 58 52 52 56 V70"/><circle cx="40" cy="30" r="14"/><circle cx="40" cy="30" r="6"/><path d="M40 10 V16 M40 44 V50 M20 30 H26 M54 30 H60 M26 16 L30 20 M50 40 L54 44 M26 44 L30 40 M50 20 L54 16"/></svg>
    <h3>Team</h3><span class="go"><svg width="10" height="12" viewBox="0 0 10 12" fill="none" stroke="#fff" stroke-width="2"><path d="M3 1 L8 6 L3 11"/></svg></span>
  </div>
  <div class="tile active" style="left:764px;top:301px">
    <svg width="60" height="70" viewBox="0 0 60 70" fill="none" stroke="#2e5ea6" stroke-width="3"><circle cx="30" cy="20" r="15"/><path d="M4 66 C4 50 12 40 22 36 C26 40 34 40 38 36 C48 40 56 50 56 66 Z"/></svg>
    <h3>Career</h3><span class="go"><svg width="10" height="12" viewBox="0 0 10 12" fill="none" stroke="#fff" stroke-width="2"><path d="M3 1 L8 6 L3 11"/></svg></span>
  </div>
</section>

<h2 class="section-title" style="left:186px;top:1194px">NEWS</h2>
<div class="title-bar" style="left:187px;top:1244px"></div>

<article class="news-card" style="left:172px">
  <div class="news-img" role="img" aria-label="Photo of a young man in a life vest fishing from a boat on blue water" style="background:linear-gradient(135deg,#2d6aa6,#1f4f86 60%,#3a5f7f)"></div>
  <h4>Lorem ipsum dolor sit amet</h4><time>December 1, 2018</time>
  <p>Sed ut perspiciatis unde omnis iste natus error[...]</p>
</article>
<article class="news-card" style="left:465px">
  <div class="news-img" role="img" aria-label="Photo of two young people in helmets at an indoor go-kart track" style="background:linear-gradient(135deg,#3a3a3a,#7a7670 50%,#a8a49c)"></div>
  <h4>Lorem ipsum dolor sit amet</h4><time>December 1, 2018</time>
  <p>Sed ut perspiciatis unde omnis iste natus error[...]</p>
</article>
<article class="news-card" style="left:756px">
  <div class="news-img" role="img" aria-label="Video still of a group in life vests rowing a boat among water lilies" style="position:relative;background:linear-gradient(135deg,#5a7a8e,#6e8a4c 55%,#3f6a2c)">
    <span class="play" style="left:117px;top:66px"><svg width="14" height="16" viewBox="0 0 14 16"><path d="M2 1 L13 8 L2 15Z" fill="#2e5ea6"/></svg></span>
  </div>
  <h4>Lorem ipsum dolor sit amet</h4><time>December 1, 2018</time>
  <p>Sed ut perspiciatis unde omnis iste natus error[...]</p>
</article>
<a class="btn" style="left:535px;top:1629px;width:129px;height:33px">View All</a>

<section class="about">
  <h2 class="section-title" style="left:183px;top:52px">ABOUT US</h2>
  <div class="title-bar" style="left:183px;top:102px;width:62px"></div>
  <p class="about-text"><b>Kelmora Sverige AB</b> carries out care and care for persons aged <b>14-25 years</b>. This is mainly done through <b>Home for Care and Housing (HVB)</b> . We are specialists in psychosocial abuse and crime problems. By constantly being open to new methods and well aware of the existing ones that work, we develop and improve the care. The methods are adapted to the individual, we do not believe that <b>ONE thought or ONE</b> perspective can be applied to everyone.</p>
  <a class="btn" style="left:183px;top:331px;width:129px;height:33px">More</a>
  <div class="abs" role="img" aria-label="Video still of a counsellor talking with a young man in a hoodie" style="left:756px;top:161px;width:270px;height:200px;background:linear-gradient(120deg,#8fa3b8,#c7ced8 50%,#d9b8c4)">
    <span class="play" style="left:117px;top:82px"><svg width="14" height="16" viewBox="0 0 14 16"><path d="M2 1 L13 8 L2 15Z" fill="#2e5ea6"/></svg></span>
  </div>
</section>

<footer>
  <div class="abs foot-logo"><span class="brand-dot"></span><span class="brand-name">Kelmora</span></div>

  <h4 class="foot-h" style="left:174px">Contact</h4>
  <div class="contact-line" style="top:2344px">
    <svg width="18" height="22" viewBox="0 0 18 22" fill="none" stroke="#8ab52d" stroke-width="1.6"><path d="M9 21 C4 14 2 11 2 8 A7 7 0 0 1 16 8 C16 11 14 14 9 21Z"/><circle cx="9" cy="8" r="2.5"/></svg>
    <span>Kelmora Sverige AB Lindvägen 22<br>241 30 Ekby</span>
  </div>
  <div class="contact-line" style="top:2400px">
    <svg width="20" height="20" viewBox="0 0 20 20" fill="none" stroke="#8ab52d" stroke-width="1.6"><path d="M4 2 L8 6 L6 9 C7 12 9 14 12 15 L14 13 L18 16 L16 19 C8 18 2 12 1 4 Z"/></svg>
    <span>010-4417260</span>
  </div>
  <div class="contact-line" style="top:2435px">
    <svg width="20" height="16" viewBox="0 0 20 16" fill="none" stroke="#8ab52d" stroke-width="1.6"><rect x="1" y="2" width="18" height="12"/><path d="M1 2 L10 9 L19 2"/></svg>
    <span>info@kelmora.se</span>
  </div>
  <div class="abs" style="left:172px;top:2476px;font-size:15px;font-weight:700;color:var(--green);letter-spacing:.8px">Org nr 559012-3344</div>
  <a class="btn" style="left:172px;top:2529px;width:165px;height:35px">Have a Query</a>

  <h4 class="foot-h" style="left:466px">kelmora.se</h4>
  <ul class="links">
    <li>About us</li><li>Team</li><li>Quality Work</li><li>Values base</li><li>Björkhagen HVB</li><li>Treament</li><li>Career</li>
  </ul>

  <h4 class="foot-h" style="left:758px">Newsletter</h4>
  <p class="abs" style="left:758px;top:2352px;font-size:13.5px;line-height:19px;color:#777;letter-spacing:.5px">Subscribe to our Newsletter<br>for latest updates</p>
  <div class="subscribe"><span>Your email |</span><b>Submit</b></div>

  <div class="social" role="img" aria-label="Small photo of a young man fishing" style="left:759px;background:linear-gradient(135deg,#2f6aa3,#5b8ab0)"><i style="background:var(--blue)"></i></div>
  <div class="social" role="img" aria-label="Small photo of a living room" style="left:842px;background:linear-gradient(135deg,#3b3b3b,#b0aca4)"><i style="background:#3f8fd6"></i></div>
  <div class="social" role="img" aria-label="Small photo of a group rowing" style="left:925px;background:linear-gradient(135deg,#4f7a3a,#6f8ea8)"><i style="background:#e0262f"></i></div>
</footer>

<div class="copyright">Copyright kelmora.se | 2018</div>
</body>
</html>
```